First Birthday Party Invitation

We need a flyer/invitation design for our baby girl Marisol's first birthday party. We want the design to look like a club event flyer. The party will have a sailing/nautical theme and will be at a marina but in Miami so the invite must have a cool, non-baby, non-kitchy vibe.

Here's the text...feel free to play around with it!

Welcome Aboard! 

We'll have lots of fun

Our little Marisol is turning one!

You're invited to a party

on Saturday, August 7th from 5 - 7 p.m.

Tide-And-Rope Miami

Third Floor
4187 North Coralwind Avenue
Miami, FL 33149-7812
Parking tickets will be validated 

Please RSVP by July 31st to MarisolBirthday@bluefinmail.test or 305.482.9067

Arrive early at 4 p.m. to join us on a short pre-party boat tour of the Miami skyline

Flyer should be one-sided only.  It will be printed in color and also emailed. 

Important update - please add small text that says "No gifts please.  A contribution to Tide And Rope's programs would be greatly appreciated."

```html
<!DOCTYPE html>
<html lang="en">
<head>
<meta charset="utf-8">
<title>Marisol's First Birthday – Welcome Aboard</title>
<link rel="stylesheet" href="https://fonts.googleapis.com/css2?family=Bowlby+One+SC&family=Federo&display=swap">
<style>
  :root {
    --navy: #100b4f;
    --paper: #ffffff;
    --sea-light: #bdeefb;
    --sea-mid: #6fd6f5;
    --sea-deep: #22c2ef;
    --drink: #2fb8ef;
    --drink-light: #8fdcf7;
  }
  html, body {
    margin: 0;
    padding: 0;
    overflow: hidden;
    background: var(--paper);
  }
  .invitation {
    position: relative;
    width: 900px;
    height: 1200px;
    overflow: hidden;
    background: var(--paper);
    color: var(--navy);
    font-family: "Federo", sans-serif;
    font-variant: small-caps;
  }
  .line {
    position: absolute;
    left: 0;
    width: 100%;
    margin: 0;
    text-align: center;
    white-space: nowrap;
    line-height: 1;
  }
  .headline {
    font-family: "Bowlby One SC", sans-serif;
    font-weight: 400;
    font-variant: normal;
  }
  .headline__text {
    display: inline-block;
    transform-origin: center;
  }
  .headline--welcome { top: 58px; font-size: 74px; }
  .headline--welcome .headline__text { transform: scaleX(0.72); }
  .headline--invited { top: 328px; font-size: 48px; }
  .headline--invited .headline__text { transform: scaleX(0.79); }

  .intro { font-size: 27px; }
  .intro--fun { top: 200px; }
  .intro--turning { top: 252px; }
  .when { top: 390px; font-size: 19px; }
  .venue-name { top: 451px; font-size: 20px; }
  .address { font-size: 20px; }
  .address--floor { top: 507px; }
  .address--street { top: 537px; }
  .address--city { top: 567px; }
  .address--parking { top: 597px; font-size: 18px; }
  .rsvp { top: 646px; font-size: 20px; }
  .early { top: 697px; font-size: 20px; }
  .gifts { top: 747px; font-size: 18px; }

  .drink-icon {
    position: absolute;
    top: 308px;
    width: 42px;
    height: 72px;
    background: linear-gradient(to bottom, var(--drink) 0 55%, var(--drink-light) 55% 100%);
    border-radius: 6px 6px 3px 3px;
  }
  .drink-icon--left { left: 118px; }
  .drink-icon--right { left: 732px; }

  .seascape {
    position: absolute;
    left: 0;
    bottom: 0;
    width: 900px;
    height: 400px;
    background: linear-gradient(to bottom,
      rgba(255, 255, 255, 0) 0%,
      var(--sea-light) 30%,
      var(--sea-mid) 65%,
      var(--sea-deep) 100%);
  }
</style>
</head>
<body>
<main class="invitation">
  <h1 class="line headline headline--welcome"><span class="headline__text">Welcome Aboard!</span></h1>

  <p class="line intro intro--fun">We'll have lots of fun</p>
  <p class="line intro intro--turning">Our little Marisol is turning one!</p>

  <div class="drink-icon drink-icon--left" role="img" aria-label="Blue cocktail glass with umbrella"></div>
  <h2 class="line headline headline--invited"><span class="headline__text">You're invited to a party</span></h2>
  <div class="drink-icon drink-icon--right" role="img" aria-label="Blue cocktail glass with umbrella"></div>

  <p class="line when">on Saturday, August 7th from 5 – 7 p.m.</p>

  <p class="line venue-name">Tide-And-Rope Miami</p>

  <p class="line address address--floor">Third Floor</p>
  <p class="line address address--street">4187 North Coralwind Avenue</p>
  <p class="line address address--city">Miami, FL 33149-7812</p>
  <p class="line address address--parking">Parking tickets will be validated</p>

  <p class="line rsvp">Please RSVP by July 31st to MarisolBirthday@bluefinmail.test or 305.482.9067</p>
  <p class="line early">Arrive early at 4 p.m. to join us on a short pre-party boat tour of the Miami skyline</p>
  <p class="line gifts">"No gifts please.&nbsp; A contribution to Tide And Rope's programs would be greatly appreciated."</p>

  <div class="seascape" role="img" aria-label="Illustration of a breaking turquoise wave beside a small island with palm trees"></div>
</main>
</body>
</html>
```